New logo and wordpress design for Brightmoor-hub.org

We run a website that collates profiles/interviews of individuals who have completed a PhD and moved away from a traditional academix career path into something related. This is often related to the field they studied in, such as publishing, government policy, consulting, teaching and many other things. The website https://brightmoor-hub.org aims to give students and researchers ideas about what paths they can take their career on.

We would like to refresh our brand with a new website and logo. Our website is run through wordpress and hence we would need appropriate files and designs to accomodate this.
Our new logo should represent the idea of navigating a career path and exploring the unknown. Up until now it has been a compass in tones of purple and blue. We are happy to keep this motif but would need an updated, more representative logo. We are also happy to get some new ideas if the designer has something they think would fit.
The website itself should have fresh and clean look. We would like a banner at the top with clear links to the various parts of the site. The banner should stay consistent throughout the site.
We would like the main page to have a clean and simple look which places the focus on the profiles and their associated photos.
We would like pictographs to represent the different fields which our profiles fit into and would like to discuss with the winning designer what these would look like exactly. As a starting point we would like pictographs representing STEM (Science, Technology, Engineering, Mathematics) and SHAPE (Social Sciences, Humanities and Arts for People and the Economy).

We are really looking for something that is clean and professional but embodies our mission to represent all of the major industries which doctoral graduates can go on to work in. Those being, academia (universities), government, industry (private enterprise and companies), and third sector (Charities and think tanks etc.). Any design should cover all of these and not focus just on a big business or similar. It should also represent that we are not purely science focused, but all disciplines and are a broad church in that sense. We are open to various colour schemes and ideas but would like something that gives a professional but approachable feel, it should have elements of Oxford, but not suggest that we are only open to Calderwick University students or graduates.
Some sites that may be useful are:
https://kestrelguild.org/news-resources/projects/research-culture/ - talks about the different areas of employment we are trying to represent
https://www.famden-lv.ac.uk/ an oxford internal website that we like the presentation of.

Target Market(s)

Academic researchers with a PhD

Industry/Entity Type

Academic Careers

Colors
0054AA
0677BA
7BADD7
CADEEF
E8F1F8
00AB8E
00BBA5
67D7C9
C6EFE9
E9F9F6
FFF300
FFF600
FEFA6F
FFFEC7
FFFEE8
6B429C
8869AF
B7A5CE
E3DAEB
F3F0F8

Requirements
Must have
• A new logo
Should not have
• The existing logo

```html
<!DOCTYPE html>
<html lang="en">
<head>
<meta charset="utf-8">
<title>Brightmoor Hub – Home page designs</title>
<link rel="stylesheet" href="https://fonts.googleapis.com/css2?family=Raleway:wght@400;500;600&family=Roboto:wght@400;500;700;900&display=swap">
<style>
:root{
  --orange:#f26a1b;
  --ink:#1e1e1e;
  --dark:#1b1b1b;
  --muted:#8a8a8a;
  --section-gray:#f3f3f3;
  --canvas-bg:#ececec;
  --white:#ffffff;
}
*{box-sizing:border-box;margin:0;padding:0}
html,body{width:787px;height:1200px;overflow:hidden;background:var(--canvas-bg)}
body{font-family:"Roboto",Arial,sans-serif;color:var(--ink)}
.canvas{position:relative;width:787px;height:1200px;overflow:hidden;background:var(--canvas-bg)}
.page{position:absolute;top:40px;width:337px;background:var(--white);overflow:hidden;box-shadow:0 1px 6px rgba(0,0,0,.08)}
.page--stem{left:41px;height:1000px}
.page--shape{left:409px;height:1119px}
.abs{position:absolute}

/* header */
.site-header{position:absolute;top:0;left:0;width:337px;height:34px;background:var(--white);z-index:3}
.brand{position:absolute;left:31px;top:8px;display:flex;align-items:center;gap:4px}
.brand-mark{width:17px;height:17px;border-radius:50%;background:#4a4a4a}
.brand-name{font-size:7.4px;font-weight:400;color:#555}
.main-nav{position:absolute;left:124px;top:13px;display:flex;align-items:center;gap:4.3px;font-size:3.5px;font-weight:700;color:var(--ink)}
.main-nav .is-current{background:var(--orange);color:#fff;padding:2px 4.5px;border-radius:5px}
.main-nav .sep{color:#999}
.search-icon{width:4px;height:4px;border:0.7px solid var(--ink);border-radius:50%}

/* hero */
.hero{position:absolute;left:0;top:34px;width:337px;height:159px}
.hero--dark{background:linear-gradient(135deg,#4a4a4a 0%,#2a2a2a 45%,#1a1a1a 100%)}
.hero--photo{background:linear-gradient(160deg,#6d7f97 0%,#8a7a63 40%,#5a4a38 75%,#3a3128 100%)}
.hero-title{position:absolute;left:0;width:337px;text-align:center;font-family:"Raleway",sans-serif;color:#fff;font-size:11.5px;font-weight:400;letter-spacing:.1px}
.hero-title--accent{color:var(--orange);font-family:"Roboto",sans-serif;font-weight:700;font-size:12px}
.hero-sub{position:absolute;left:0;width:337px;text-align:center;color:#fff;font-size:5.2px;line-height:8.3px}
.toggle{position:absolute;height:13px;padding:0 9px;border-radius:7px;font-size:4.5px;font-weight:700;line-height:13px;background:#fff;color:var(--ink)}
.toggle.is-active{background:var(--orange);color:#fff}
.hero-wave{position:absolute;left:0;top:0}

/* field circles */
.field{position:absolute;width:48px;height:48px;margin-left:-24px;border:1.3px solid var(--orange);border-radius:50%;background:#fff;text-align:center;font-size:22px;font-weight:900;line-height:46px;color:var(--ink)}
.field.is-active{background:var(--orange);color:#fff}
.field-icon{position:absolute;left:12px;top:35px;width:22px;height:22px;border-radius:50%;background:var(--orange);display:flex;align-items:center;justify-content:center}
.field.is-active .field-icon{background:#fff}
.field-label{position:absolute;width:80px;margin-left:-40px;text-align:center;font-size:5px;font-weight:500;color:var(--ink)}
.field-label.is-active{color:var(--orange);text-decoration:underline}

/* profile cards */
.profile-card{position:absolute;width:85px;height:113px;background:#fff;border-radius:7px;box-shadow:0 1px 4px rgba(0,0,0,.16);text-align:center}
.profile-card.is-active{border:1px solid var(--orange)}
.avatar{position:absolute;left:22px;top:-20px;width:41px;height:41px;border-radius:50%;background:linear-gradient(160deg,#8b95a3,#3b4756)}
.profile-card.is-active .avatar{border:1.3px solid var(--orange);background:linear-gradient(160deg,#4d6b8a,#1e2a44)}
.avatar--warm{background:linear-gradient(160deg,#d9c9a8,#7a6a57)}
.profile-name{position:absolute;top:29px;width:100%;font-size:4.8px;font-weight:700}
.profile-role{position:absolute;top:37px;left:6px;right:6px;font-size:3.5px;line-height:6px;font-weight:500;color:var(--orange)}
.profile-date{position:absolute;top:52px;width:100%;font-size:3px;color:var(--muted)}
.profile-facts{position:absolute;top:61px;width:100%;font-size:3.4px;line-height:6.2px;font-weight:700}
.btn{position:absolute;height:10px;border-radius:5px;border:0.8px solid var(--orange);background:#fff;color:var(--ink);font-size:3.5px;font-weight:700;line-height:9px;text-align:center}
.btn.is-filled{background:var(--orange);color:#fff}
.profile-card .btn{left:23px;top:91px;width:39px}
.arrow{position:absolute;width:11px;height:11px;border-radius:50%;display:flex;align-items:center;justify-content:center}
.arrow--prev{border:0.8px solid var(--orange);background:#fff}
.arrow--next{background:var(--orange)}

/* sections */
.band-gray{position:absolute;left:0;width:337px;background:var(--section-gray)}
.section-title{position:absolute;left:0;width:337px;text-align:center;font-family:"Raleway",sans-serif;font-weight:500;font-size:10.4px;line-height:13.3px;color:var(--ink)}
.title-rule{position:absolute;width:20px;height:1px;background:var(--orange);left:158px}
.intro{position:absolute;left:37px;width:263px;text-align:center;font-size:3.9px;line-height:7.2px;color:#333}

/* info cards */
.info-card{position:absolute;width:85px;height:120px;background:#fff;border-radius:7px;box-shadow:0 1px 4px rgba(0,0,0,.16);text-align:center}
.info-card.is-active{border:1px solid var(--orange)}
.info-photo{position:absolute;left:2px;top:2px;width:81px;height:61px;border-radius:6px 6px 0 0}
.photo--meeting{background:linear-gradient(150deg,#e8e4de,#8c8279 60%,#3a3533)}
.photo--city{background:linear-gradient(180deg,#9db3c9 0%,#b69d72 45%,#6f5a3f 100%)}
.photo--team{background:linear-gradient(150deg,#c9ccd0,#6b7784 55%,#2f3944)}
.info-title{position:absolute;top:70px;width:100%;font-size:5px;font-weight:700}
.info-text{position:absolute;top:78px;left:8px;right:8px;font-size:3.5px;line-height:6.2px;color:#444}
.info-card .btn{top:104px}

/* get ready */
.ready-photo{position:absolute;width:157px;height:115px;border-radius:10px;background:linear-gradient(120deg,#dfe5ea 0%,#a38b6c 45%,#6d5a48 75%,#cfd4d8 100%)}
.ready-box{position:absolute;width:138px;height:117px;background:#fff;border:1px solid var(--orange);border-radius:9px}
.ready-title{position:absolute;left:13px;top:18px;font-family:"Raleway",sans-serif;font-weight:500;font-size:10.4px;line-height:13.3px}
.ready-title span{border-bottom:1px solid var(--orange)}
.ready-text{position:absolute;left:13px;top:55px;width:115px;font-size:4.1px;line-height:7.6px;color:#333}
.ready-box .btn{left:13px;top:83px;width:39px;height:12px;line-height:11px}

/* footer */
.site-footer{position:absolute;left:0;width:337px;background:var(--dark);color:#fff}
.footer-inner{position:absolute;left:0;width:337px;height:75px}
.footer-logo{position:absolute;left:31px;top:22px;width:62px;height:15px;background:#fff;display:flex;align-items:center;gap:3px;padding-left:3px}
.footer-logo .brand-mark{width:11px;height:11px}
.footer-logo .brand-name{font-size:5px}
.footer-heading{position:absolute;top:0;font-size:4.6px;font-weight:700}
.footer-list{position:absolute;top:9px;list-style:none;font-size:3.4px;line-height:8.1px}
.footer-list li{display:flex;align-items:center;gap:4px}
.footer-list li::before{content:"";width:3px;height:3px;border-radius:50%;background:var(--orange)}
.newsletter{position:absolute;left:230px;top:10px;width:75px;height:13px;border-radius:7px;background:#fff}
.newsletter-field{position:absolute;left:5px;top:0;font-size:3.6px;line-height:13px;color:#666}
.newsletter-btn{position:absolute;right:1px;top:1px;width:30px;height:11px;border-radius:6px;background:var(--orange);font-size:3.6px;font-weight:700;line-height:11px;text-align:center}
.social{position:absolute;top:30px;width:10px;height:10px;border-radius:50%;border:0.8px solid var(--orange)}
.social.is-filled{background:var(--orange)}
.footer-rule{position:absolute;left:31px;top:60px;width:275px;height:0.5px;background:#3a3a3a}
.copyright{position:absolute;top:66px;width:337px;text-align:center;font-size:3.2px;color:#ddd}
</style>
</head>
<body>
<main class="canvas">

  <!-- STEM home page -->
  <section class="page page--stem" aria-label="Home page, STEM view">
    <header class="site-header">
      <div class="brand"><span class="brand-mark"></span><span class="brand-name">Brightmoor Hub</span></div>
      <nav class="main-nav"><span class="is-current">HOME</span><span>CAREER PROFILES</span><span>GET INVOLVED</span><span>EVENTS</span><span>RESOURCES</span><span>ABOUT US</span><span class="sep">|</span><span class="search-icon"></span></nav>
    </header>

    <div class="hero hero--dark" role="img" aria-label="Dark grey faceted polygon background"></div>
    <h1 class="hero-title" style="top:75px">EXPLORE YOUR OPTIONS</h1>
    <p class="hero-title hero-title--accent" style="top:90px">BEYOND ACADEMIA</p>
    <p class="hero-sub" style="top:107px">A collection of profiles of people who have made the transition<br>from academia to industry.</p>
    <span class="toggle is-active" style="left:136px;top:130px">STEM</span>
    <span class="toggle" style="left:170px;top:130px">SHAPE</span>

    <div class="field" style="left:83px;top:168px">S<span class="field-icon"><svg width="12" height="12" viewBox="0 0 12 12"><circle cx="6" cy="6" r="4" fill="none" stroke="#fff" stroke-width="1.4"/></svg></span></div>
    <div class="field" style="left:140px;top:168px">T<span class="field-icon"><svg width="12" height="12" viewBox="0 0 12 12"><rect x="2.5" y="2.5" width="7" height="7" fill="none" stroke="#fff" stroke-width="1.4"/></svg></span></div>
    <div class="field is-active" style="left:197px;top:168px">E<span class="field-icon"><svg width="12" height="12" viewBox="0 0 12 12"><path d="M2 8 A4 4 0 0 1 10 8 Z" fill="#222"/><rect x="1.5" y="8" width="9" height="1.5" fill="#222"/></svg></span></div>
    <div class="field" style="left:254px;top:168px">M<span class="field-icon"><svg width="12" height="12" viewBox="0 0 12 12" stroke="#fff" stroke-width="1.2"><path d="M1.5 3.5h4M3.5 1.5v4M7 3.5h3.5M2 8l3 3M5 8l-3 3M7 8.5h3.5M7 10.5h3.5"/></svg></span></div>
    <span class="field-label" style="left:83px;top:232px">SCIENCE</span>
    <span class="field-label" style="left:140px;top:232px">TECHNOLOGY</span>
    <span class="field-label is-active" style="left:197px;top:232px">ENGINEERING</span>
    <span class="field-label" style="left:254px;top:232px">MATHEMATICS</span>

    <span class="arrow arrow--prev" style="left:10px;top:328px"><svg width="5" height="5" viewBox="0 0 5 5"><path d="M3.3 .8 1.5 2.5 3.3 4.2" fill="none" stroke="#222" stroke-width=".8"/></svg></span>
    <span class="arrow arrow--next" style="left:315px;top:328px"><svg width="5" height="5" viewBox="0 0 5 5"><path d="M1.7 .8 3.5 2.5 1.7 4.2" fill="none" stroke="#fff" stroke-width=".8"/></svg></span>

    <article class="profile-card" style="left:31px;top:277px">
      <div class="avatar" role="img" aria-label="Portrait photo of Tomas Halvorsen"></div>
      <h3 class="profile-name">TOMAS HALVORSEN</h3>
      <p class="profile-role">QUALITY ENGINEER AT NORVALE GROUP (PELTIS MEDICAL GMBH)</p>
      <p class="profile-date">Published March 28, 2024</p>
      <p class="profile-facts">CAREER PROFILES: PHD<br>DEGREE: BIOMEDICAL ENGINEERING<br>LEFT ACADEMIA AFTER: PHD<br>SECTOR: BIOMEDICAL MATERIALS</p>
      <span class="btn">VIEW PROFILE</span>
    </article>
    <article class="profile-card is-active" style="left:125px;top:277px">
      <div class="avatar" role="img" aria-label="Portrait photo of Ravi Kestner in graduation gown"></div>
      <h3 class="profile-name">RAVI KESTNER</h3>
      <p class="profile-role">SENIOR PRINCIPAL SCIENTIST<br>AT QUENBY PHARMA</p>
      <p class="profile-date">Published July 25, 2023</p>
      <p class="profile-facts">CAREER PROFILES: PHD<br>DEGREE: ENGINEERING SCIENCE<br>LEFT ACADEMIA AFTER: PHD<br>SECTOR: PHARMACEUTICALS</p>
      <span class="btn is-filled">VIEW PROFILE</span>
    </article>
    <article class="profile-card" style="left:220px;top:277px">
      <div class="avatar avatar--warm" role="img" aria-label="Portrait photo of Clara Wendell"></div>
      <h3 class="profile-name">CLARA WENDELL</h3>
      <p class="profile-role">SENIOR DATA SCIENTIST AT VELTRUM DATA AND ANALYTICS</p>
      <p class="profile-date">Published March 27, 2023</p>
      <p class="profile-facts">CAREER PROFILES: PHD<br>DEGREE: ENGINEERING SCIENCE<br>LEFT ACADEMIA AFTER: 0-3 YEARS POSTDOC<br>SECTOR: CONSULTING</p>
      <span class="btn">VIEW PROFILE</span>
    </article>

    <div class="band-gray" style="top:423px;height:277px"></div>
    <h2 class="section-title" style="top:447px">RESEARCHERS FIND ALL SORTS OF<br>REWARDING CAREERS – SMART PEOPLE<br>WORK EVERYWHERE!</h2>
    <span class="title-rule" style="top:490px"></span>
    <p class="intro" style="top:497px">Such diversity in potential roles can prove challenging when exploring your options. This collection of career profiles enables you to see what others in your position chose to do, why and how they made the move, and what they most enjoy about their job. You will get a feel for their daily activities, workplace culture and work-life balance.Top tip: Look out for authors' insights into which skills developed during or after their PhD proved helpful in getting their job, and performing well there. You'll be encouraged to see how people are building on their research expertise to thrive in newer roles.And don't miss the "employer bio" at the end of each career profile for careers opportunities in each organisation.</p>

    <article class="info-card" style="left:31px;top:551px">
      <div class="info-photo photo--meeting" role="img" aria-label="Photo of a handshake at a job interview"></div>
      <h3 class="info-title">CAREER PROFILES</h3>
      <p class="info-text">Explore a collection of profiles from researchers pursuing careers beyond academia.</p>
      <span class="btn" style="left:19px;width:47px">EXPLORE PROFILES</span>
    </article>
    <article class="info-card is-active" style="left:125px;top:551px">
      <div class="info-photo photo--city" role="img" aria-label="Aerial photo of historic university buildings"></div>
      <h3 class="info-title">ABOUT US</h3>
      <p class="info-text">This website is edited by a group of DPhil students and researchers connected to Calderwick University.</p>
      <span class="btn is-filled" style="left:19px;width:47px">WHO WE ARE</span>
    </article>
    <article class="info-card" style="left:220px;top:551px">
      <div class="info-photo photo--team" role="img" aria-label="Photo of colleagues working in an open office"></div>
      <h3 class="info-title">GET INVOLVED</h3>
      <p class="info-text">See how you can contribute to the Brightmoor Hub: Options Beyond Academia project.</p>
      <span class="btn" style="left:19px;width:47px">FIND OUT HOW</span>
    </article>

    <div class="ready-photo" style="left:149px;top:734px" role="img" aria-label="Photo of a smiling team around a meeting table"></div>
    <div class="ready-box" style="left:31px;top:755px">
      <h2 class="ready-title">GET READY TO<br><span>START?</span></h2>
      <p class="ready-text">If you're a DPhil student or member of research staff at the Calderwick University, you can join the editorial team! Please contact us to find out more.</p>
      <span class="btn is-filled">CONTACT US</span>
    </div>

    <footer class="site-footer" style="top:904px;height:96px">
      <div class="footer-inner" style="top:21px">
        <div class="footer-logo"><span class="brand-mark"></span><span class="brand-name" style="color:#555">Brightmoor Hub</span></div>
        <h4 class="footer-heading" style="left:102px">COMPANY</h4>
        <ul class="footer-list" style="left:102px"><li>HOME</li><li>CAREER PROFILES</li><li>GET INVOLVED</li><li>EVENTS</li><li>RESOURCES</li><li>ABOUT US</li></ul>
        <h4 class="footer-heading" style="left:150px">ABOUT</h4>
        <ul class="footer-list" style="left:150px"><li>Marisol Ortega-Lind June 12, 2024</li><li>Henry Aldous May 21, 2024</li><li>Priya Solanki April 2, 2024</li><li>Nira Desai April 2, 2024</li><li>Tomas Halvorsen March 28, 2024</li></ul>
        <h4 class="footer-heading" style="left:230px">JOIN NEWSLETTER</h4>
        <div class="newsletter"><span class="newsletter-field">Email Address</span><span class="newsletter-btn">JOIN NOW</span></div>
        <span class="social is-filled" style="left:230px"></span>
        <span class="social" style="left:242px"></span>
        <span class="social" style="left:254px"></span>
        <span class="footer-rule"></span>
        <p class="copyright">© 2024 <b>BRIGHTMOOR HUB</b> &nbsp;|&nbsp; All Rights Reserved</p>
      </div>
    </footer>
  </section>

  <!-- SHAPE home page -->
  <section class="page page--shape" aria-label="Home page, SHAPE view">
    <header class="site-header">
      <div class="brand"><span class="brand-mark"></span><span class="brand-name">Brightmoor Hub</span></div>
      <nav class="main-nav"><span class="is-current">HOME</span><span>CAREER PROFILES</span><span>GET INVOLVED</span><span>EVENTS</span><span>RESOURCES</span><span>ABOUT US</span><span class="sep">|</span><span class="search-icon"></span></nav>
    </header>

    <div class="hero hero--photo" role="img" aria-label="Photo of historic university domes and spires under a blue sky"></div>
    <svg class="hero-wave" style="top:34px" width="337" height="160" viewBox="0 0 337 160">
      <path d="M0 118 C50 150 110 162 175 150 C240 138 285 118 337 122 L337 160 L0 160Z" fill="#fff"/>
      <path d="M160 150 C220 122 285 108 337 112 L337 142 C300 124 250 128 195 146Z" fill="var(--orange)"/>
    </svg>
    <span class="abs" style="left:158px;top:162px;width:22px;height:22px;border-radius:50%;background:#fff;box-shadow:0 1px 3px rgba(0,0,0,.2)"><span class="brand-mark abs" style="left:5px;top:5px;width:12px;height:12px"></span></span>
    <h1 class="hero-title" style="top:77px">EXPLORE YOUR OPTIONS</h1>
    <p class="hero-title hero-title--accent" style="top:92px">BEYOND ACADEMIA</p>
    <p class="hero-sub" style="top:110px">A collection of profiles of people who have made the transition<br>from academia to industry.</p>

    <h2 class="section-title" style="top:223px;font-size:11px">RECENT PROFILES</h2>
    <span class="title-rule" style="top:244px"></span>
    <p class="abs" style="left:142px;top:248px;font-size:5px;font-weight:500">STEM &nbsp;&nbsp;&nbsp;<span style="color:#888">|</span>&nbsp;&nbsp;&nbsp; <span style="color:var(--orange);text-decoration:underline">SHAPE</span></p>

    <div class="field" style="left:58px;top:264px">S<span class="field-icon"><svg width="12" height="12" viewBox="0 0 12 12"><circle cx="6" cy="6" r="4" fill="none" stroke="#fff" stroke-width="1.4"/></svg></span></div>
    <div class="field" style="left:113px;top:264px">H<span class="field-icon"><svg width="12" height="12" viewBox="0 0 12 12"><circle cx="6" cy="4" r="2" fill="#fff"/><path d="M2 10 Q6 6 10 10" fill="none" stroke="#fff" stroke-width="1.4"/></svg></span></div>
    <div class="field is-active" style="left:168px;top:264px">A<span class="field-icon"><svg width="12" height="12" viewBox="0 0 12 12"><path d="M6 1.5 10 6 6 10.5 2 6Z" fill="#222"/></svg></span></div>
    <div class="field" style="left:224px;top:264px">P<span class="field-icon"><svg width="12" height="12" viewBox="0 0 12 12" fill="#fff"><circle cx="6" cy="3.5" r="1.6"/><circle cx="2.8" cy="5" r="1.2"/><circle cx="9.2" cy="5" r="1.2"/><rect x="4.2" y="6" width="3.6" height="4" rx="1"/></svg></span></div>
    <div class="field" style="left:279px;top:264px">E<span class="field-icon"><svg width="12" height="12" viewBox="0 0 12 12"><circle cx="6" cy="6" r="4.2" fill="none" stroke="#fff" stroke-width="1.2"/><circle cx="6" cy="6" r="1.8" fill="#fff"/></svg></span></div>
    <span class="field-label" style="left:58px;top:327px">SOCIAL SCIENCES</span>
    <span class="field-label" style="left:113px;top:327px">HUMANITIES</span>
    <span class="field-label is-active" style="left:168px;top:327px">ARTS</span>
    <span class="field-label" style="left:224px;top:327px">PEOPLE</span>
    <span class="field-label" style="left:279px;top:327px">ECONOMY</span>

    <span class="arrow arrow--prev" style="left:10px;top:420px"><svg width="5" height="5" viewBox="0 0 5 5"><path d="M3.3 .8 1.5 2.5 3.3 4.2" fill="none" stroke="#222" stroke-width=".8"/></svg></span>
    <span class="arrow arrow--next" style="left:315px;top:420px"><svg width="5" height="5" viewBox="0 0 5 5"><path d="M1.7 .8 3.5 2.5 1.7 4.2" fill="none" stroke="#fff" stroke-width=".8"/></svg></span>

    <article class="profile-card" style="left:31px;top:369px">
      <div class="avatar" role="img" aria-label="Portrait photo of Tomas Halvorsen"></div>
      <h3 class="profile-name">TOMAS HALVORSEN</h3>
      <p class="profile-role">QUALITY ENGINEER AT NORVALE GROUP (PELTIS MEDICAL GMBH)</p>
      <p class="profile-date">Published March 28, 2024</p>
      <p class="profile-facts">CAREER PROFILES: PHD<br>DEGREE: BIOMEDICAL ENGINEERING<br>LEFT ACADEMIA AFTER: PHD<br>SECTOR: BIOMEDICAL MATERIALS</p>
      <span class="btn">VIEW PROFILE</span>
    </article>
    <article class="profile-card is-active" style="left:125px;top:369px">
      <div class="avatar" role="img" aria-label="Portrait photo of Ravi Kestner in graduation gown"></div>
      <h3 class="profile-name">RAVI KESTNER</h3>
      <p class="profile-role">SENIOR PRINCIPAL SCIENTIST<br>AT QUENBY PHARMA</p>
      <p class="profile-date">Published July 25, 2023</p>
      <p class="profile-facts">CAREER PROFILES: PHD<br>DEGREE: ENGINEERING SCIENCE<br>LEFT ACADEMIA AFTER: PHD<br>SECTOR: PHARMACEUTICALS</p>
      <span class="btn is-filled">VIEW PROFILE</span>
    </article>
    <article class="profile-card" style="left:219px;top:369px">
      <div class="avatar avatar--warm" role="img" aria-label="Portrait photo of Clara Wendell"></div>
      <h3 class="profile-name">CLARA WENDELL</h3>
      <p class="profile-role">SENIOR DATA SCIENTIST AT VELTRUM DATA AND ANALYTICS</p>
      <p class="profile-date">Published March 27, 2023</p>
      <p class="profile-facts">CAREER PROFILES: PHD<br>DEGREE: ENGINEERING SCIENCE<br>LEFT ACADEMIA AFTER: 0-3 YEARS POSTDOC<br>SECTOR: CONSULTING</p>
      <span class="btn">VIEW PROFILE</span>
    </article>

    <div class="band-gray" style="top:518px;height:182px"></div>
    <div class="ready-photo" style="left:150px;top:540px;height:116px" role="img" aria-label="Photo of a smiling team around a meeting table"></div>
    <div class="ready-box" style="left:31px;top:561px">
      <h2 class="ready-title">GET READY TO<br><span>START?</span></h2>
      <p class="ready-text">If you're a DPhil student or member of research staff at the Calderwick University, you can join the editorial team! Please contact us to find out more.</p>
      <span class="btn is-filled">CONTACT US</span>
    </div>

    <h2 class="section-title" style="top:732px">RESEARCHERS FIND ALL SORTS OF<br>REWARDING CAREERS – SMART PEOPLE<br>WORK EVERYWHERE!</h2>
    <span class="title-rule" style="top:775px"></span>
    <p class="intro" style="top:783px">Such diversity in potential roles can prove challenging when exploring your options. This collection of career profiles enables you to see what others in your position chose to do, why and how they made the move, and what they most enjoy about their job. You will get a feel for their daily activities, workplace culture and work-life balance.Top tip: Look out for authors' insights into which skills developed during or after their PhD proved helpful in getting their job, and performing well there. You'll be encouraged to see how people are building on their research expertise to thrive in newer roles.And don't miss the "employer bio" at the end of each career profile for careers opportunities in each organisation.</p>

    <article class="info-card" style="left:31px;top:836px">
      <div class="info-photo photo--meeting" role="img" aria-label="Photo of a handshake at a job interview"></div>
      <h3 class="info-title">CAREER PROFILES</h3>
      <p class="info-text">Explore a collection of profiles from researchers pursuing careers beyond academia.</p>
      <span class="btn" style="left:19px;width:47px">EXPLORE PROFILES</span>
    </article>
    <article class="info-card is-active" style="left:125px;top:836px">
      <div class="info-photo photo--city" role="img" aria-label="Aerial photo of historic university buildings"></div>
      <h3 class="info-title">ABOUT US</h3>
      <p class="info-text">This website is edited by a group of DPhil students and researchers connected to Calderwick University.</p>
      <span class="btn is-filled" style="left:19px;width:47px">WHO WE ARE</span>
    </article>
    <article class="info-card" style="left:219px;top:836px">
      <div class="info-photo photo--team" role="img" aria-label="Photo of colleagues working in an open office"></div>
      <h3 class="info-title">GET INVOLVED</h3>
      <p class="info-text">See how you can contribute to the Brightmoor Hub: Options Beyond Academia project.</p>
      <span class="btn" style="left:19px;width:47px">FIND OUT HOW</span>
    </article>

    <svg class="abs" style="left:0;top:985px" width="337" height="47" viewBox="0 0 337 47">
      <path d="M0 16 C60 4 130 8 200 6 C250 4 300 20 337 40 L337 47 L0 47Z" fill="var(--orange)"/>
      <path d="M0 47 C60 24 130 30 200 14 C250 2 300 14 337 38 L337 47Z" fill="var(--dark)"/>
    </svg>
    <footer class="site-footer" style="top:1030px;height:89px">
      <div class="footer-inner" style="top:12px">
        <div class="footer-logo"><span class="brand-mark"></span><span class="brand-name" style="color:#555">Brightmoor Hub</span></div>
        <h4 class="footer-heading" style="left:102px">COMPANY</h4>
        <ul class="footer-list" style="left:102px"><li>HOME</li><li>CAREER PROFILES</li><li>GET INVOLVED</li><li>EVENTS</li><li>RESOURCES</li><li>ABOUT US</li></ul>
        <h4 class="footer-heading" style="left:150px">ABOUT</h4>
        <ul class="footer-list" style="left:150px"><li>Marisol Ortega-Lind June 12, 2024</li><li>Henry Aldous May 21, 2024</li><li>Priya Solanki April 2, 2024</li><li>Nira Desai April 2, 2024</li><li>Tomas Halvorsen March 28, 2024</li></ul>
        <h4 class="footer-heading" style="left:230px">JOIN NEWSLETTER</h4>
        <div class="newsletter"><span class="newsletter-field">Email Address</span><span class="newsletter-btn">JOIN NOW</span></div>
        <span class="social is-filled" style="left:230px"></span>
        <span class="social" style="left:242px"></span>
        <span class="social" style="left:254px"></span>
        <p class="copyright">© 2024 <b>BRIGHTMOOR HUB</b> &nbsp;|&nbsp; All Rights Reserved</p>
      </div>
    </footer>
  </section>

</main>
</body>
</html>
```